Quorvantelline.com

I need a site that I can sell dewatering equipment to the construction industry.
Ie, pipes fittings pumps and other such things needed to remove the groundwater on construction sites. Here in Florida, it’s needed almost everywhere seeing we are at sea level.
I want to be able to sell these products on the site and receive

Coded - Design and coding required

1 page

```html
<!DOCTYPE html>
<html lang="en">
<head>
<meta charset="utf-8">
<title>Quorvantelline.com — Dewatering Equipment</title>
<link rel="stylesheet" href="https://fonts.googleapis.com/css2?family=Poppins:ital,wght@0,400;0,500;0,600;0,700;1,400&family=Oswald:wght@500;600&display=swap">
<style>
:root{
  --blue:#12a8d3;
  --orange:#f9b200;
  --ink:#1f1f1f;
  --muted:#6b6b6b;
  --line:#dcdcdc;
  --grey-bg:#f3f3f3;
  --footer:#03333a;
  --footer-deep:#021f24;
  --white:#ffffff;
}
*{box-sizing:border-box;margin:0;padding:0}
html,body{width:1200px;height:3197px;overflow:hidden}
body{position:relative;font-family:"Poppins",sans-serif;color:var(--ink);background:var(--white)}
.abs{position:absolute}
.btn{position:absolute;display:flex;align-items:center;justify-content:center;background:var(--orange);color:var(--white);font-size:13px;font-weight:500;border-radius:20px;height:36px;width:110px}
.sec-title{position:absolute;left:85px;font-size:22px;font-weight:600}
.sec-title::after{content:"";position:absolute;left:0;top:40px;width:58px;height:3px;background:var(--orange)}
.arrows{position:absolute;left:1061px;display:flex;gap:6px}
.arrows span{width:22px;height:22px;border:1.5px solid #555;border-radius:50%;display:flex;align-items:center;justify-content:center}
.photo{position:absolute}

/* hero */
.hero{left:0;top:0;width:1200px;height:554px;background:linear-gradient(180deg,#6d5a44 0%,#4a3c2e 45%,#3b3129 100%)}
.hero-shade{left:0;top:0;width:1200px;height:554px;background:rgba(0,0,0,.35)}
.nav{left:85px;top:26px;width:1027px;height:64px;background:var(--white);border-radius:4px;box-shadow:0 2px 8px rgba(0,0,0,.2)}
.logo{position:absolute;left:30px;top:15px;font-family:"Oswald",sans-serif;font-weight:600;font-size:25px;color:var(--blue)}
.menu{position:absolute;top:22px;font-size:14px}
.phone{position:absolute;left:826px;top:16px;display:flex;align-items:center;gap:12px;font-size:15px}
.phone i{width:34px;height:34px;border:1.5px solid var(--blue);border-radius:50%;display:flex;align-items:center;justify-content:center}
.hero h1{position:absolute;left:0;width:1200px;top:196px;text-align:center;color:var(--white);font-size:44px;font-weight:700;letter-spacing:1px}
.hero p{position:absolute;left:180px;width:840px;top:266px;text-align:center;color:var(--white);font-size:14px;line-height:23px}
.dots{left:573px;top:492px;display:flex;gap:6px}
.dots span{width:13px;height:13px;border-radius:50%;background:var(--white)}
.dots span.on{background:var(--orange)}

/* services */
.service{position:absolute;top:614px;width:326px;height:283px;text-align:center}
.service.active{background:var(--blue);color:var(--white)}
.service svg{position:absolute;left:129px;top:20px}
.service h3{position:absolute;top:94px;width:100%;font-size:20px;font-weight:600}
.service p{position:absolute;top:126px;left:28px;width:270px;font-size:13.5px;line-height:22px;color:var(--muted)}
.service.active p{color:var(--white)}
.service .btn{top:216px;left:108px}

/* about */
.band-left{left:0;top:959px;width:1200px;height:202px;background:var(--blue)}
.about-card{left:85px;top:1029px;width:1027px;height:430px;background:var(--white)}
.about-text{left:107px;top:1144px;width:560px;font-size:13.5px;line-height:23px;color:var(--muted)}
.about-text p+p{margin-top:20px}
.about-photo{left:701px;top:1078px;width:499px;height:354px;background:linear-gradient(135deg,#8a8f8e 0%,#c9a51c 45%,#5e5a4f 75%,#b03a2a 100%)}

/* products */
.product{position:absolute;top:1551px;width:237px;height:245px;border:1px solid var(--line);background:var(--white)}
.product .photo{left:20px;top:20px;width:195px;height:203px;border-radius:6px}
.product.active{background:var(--blue);border-color:var(--blue)}
.product-name{position:absolute;top:1810px;width:237px;text-align:center;font-size:15px;font-weight:500}

/* projects */
.projects{left:0;top:1894px;width:1200px;height:514px;background:var(--grey-bg)}
.project .photo{top:1995px;width:325px;height:287px}
.project h4{position:absolute;top:2300px;width:325px;text-align:center;font-size:18px;font-weight:500}
.project p{position:absolute;top:2334px;width:325px;text-align:center;font-size:13.5px;color:var(--muted)}

/* testimonials */
.quote{position:absolute;top:2525px;width:499px;height:147px;border:1px solid var(--line);padding:20px 20px;font-size:12.5px;line-height:22px;font-style:italic;color:var(--muted)}
.avatar{position:absolute;top:2658px;width:56px;height:56px;border-radius:50%;background:#9c8a7c;border:3px solid var(--white)}
.author{position:absolute;top:2684px;font-size:13px;color:var(--blue)}

/* clients */
.clients{left:85px;top:2832px;width:1027px;height:79px;border:1px solid var(--line);display:flex}
.clients div{flex:1;border-right:1px solid var(--line);display:flex;align-items:center;justify-content:center;gap:8px;font-size:15px;font-weight:600;color:#4d4d4d}
.clients div:last-child{border-right:none}
.clients i{width:20px;height:20px;border-radius:50%;background:#9a9a9a;display:block}

/* footer */
.footer{left:0;top:2973px;width:1200px;height:224px;background:var(--footer);color:var(--white)}
.footer .flogo{position:absolute;left:85px;top:28px;font-family:"Oswald",sans-serif;font-size:26px;font-weight:600}
.footer .tag{position:absolute;left:85px;top:67px;font-size:13px;color:var(--blue)}
.footer .ftext{position:absolute;left:85px;top:96px;width:740px;font-size:13px;line-height:22px;color:#d8e2e3}
.social{position:absolute;left:85px;top:150px;display:flex;gap:14px}
.social span{width:20px;height:20px;background:var(--white);border-radius:3px}
.contact h5{position:absolute;left:874px;top:28px;font-size:18px;font-weight:500}
.contact .addr{position:absolute;left:900px;top:78px;font-size:13px;line-height:20px}
.contact .tel{position:absolute;top:134px;font-size:13px;display:flex;gap:8px;align-items:center}
.copy{left:0;top:3162px;width:1200px;height:35px;background:var(--footer-deep);color:var(--white);font-size:12px;padding:9px 85px}
.copy a{color:var(--blue);text-decoration:none}
</style>
</head>
<body>

<!-- Hero -->
<div class="abs hero" role="img" aria-label="Workers on a muddy construction site with a dewatering pump"></div>
<div class="abs hero-shade"></div>
<nav class="abs nav">
  <div class="logo">Quorvantelline.com</div>
  <span class="menu" style="left:278px">Home</span>
  <span class="menu" style="left:373px">About Us</span>
  <span class="menu" style="left:489px">Products</span>
  <span class="menu" style="left:607px">News</span>
  <span class="menu" style="left:698px">Contact us</span>
  <div class="phone"><i><svg width="16" height="16" viewBox="0 0 24 24"><path d="M6.6 10.8a15 15 0 0 0 6.6 6.6l2.2-2.2a1 1 0 0 1 1-.25 11 11 0 0 0 3.6.6 1 1 0 0 1 1 1V20a1 1 0 0 1-1 1A17 17 0 0 1 3 4a1 1 0 0 1 1-1h3.5a1 1 0 0 1 1 1 11 11 0 0 0 .6 3.6 1 1 0 0 1-.25 1z" fill="#12a8d3"/></svg></i>0940 - 555-218</div>
</nav>
<section class="hero abs" style="background:none">
  <h1>DEWATERING EQUIPMENT</h1>
  <p>Sed ut perspiciatis unde omnis iste natus error sit voluptatem accusantium doloremque laudantium, totam rem aperiam, eaque ipsa quae ab illo inventore veritatis et quasi architecto beatae vitae</p>
  <span class="btn" style="left:543px;top:337px">Learn More</span>
  <div class="abs dots" style="top:492px"><span></span><span></span><span class="on"></span></div>
</section>

<!-- Services -->
<div class="service" style="left:85px">
  <svg width="68" height="60" viewBox="0 0 68 60"><g fill="none" stroke="#12a8d3" stroke-width="6" stroke-linecap="round"><path d="M14 8h40a6 6 0 0 1 0 12H14a6 6 0 0 0 0 12h40a6 6 0 0 1 0 12H14a6 6 0 0 0 0 12h40"/></g></svg>
  <h3>Construction Dewatering</h3>
  <p>Sed ut perspiciatis unde omnis iste natus error sit voluptatem accusantium doloremque laudantium</p>
  <span class="btn">Learn More</span>
</div>
<div class="service active" style="left:437px">
  <svg width="68" height="60" viewBox="0 0 68 60"><g fill="none" stroke="#fff" stroke-width="4"><rect x="14" y="14" width="40" height="30" rx="4"/><path d="M22 14v30M30 14v30M38 14v30M46 14v30M4 24h10v10H4M54 24h10v10H54M24 6h20v8M20 44v8M48 44v8"/></g></svg>
  <h3>Pumps and Equipment</h3>
  <p>Sed ut perspiciatis unde omnis iste natus error sit voluptatem accusantium doloremque laudantium</p>
  <span class="btn">Learn More</span>
</div>
<div class="service" style="left:788px">
  <svg width="68" height="60" viewBox="0 0 68 60"><g fill="#12a8d3"><rect x="2" y="30" width="22" height="16" rx="3"/><rect x="44" y="30" width="22" height="16" rx="3"/><rect x="22" y="26" width="24" height="24" rx="6"/><rect x="31" y="10" width="6" height="16"/><rect x="20" y="4" width="28" height="6" rx="3"/></g></svg>
  <h3>Bypass Pumping</h3>
  <p>Sed ut perspiciatis unde omnis iste natus error sit voluptatem accusantium doloremque laudantium</p>
  <span class="btn">Learn More</span>
</div>

<!-- About -->
<div class="abs band-left"></div>
<div class="abs" style="left:1112px;top:1161px;width:88px;height:0"></div>
<div class="abs about-card"></div>
<div class="abs" style="left:0;top:1161px;width:85px;height:0"></div>
<h2 class="sec-title" style="left:107px;top:1072px">About Our Company</h2>
<div class="abs about-text">
  <p>Sed ut perspiciatis unde omnis iste natus error sit voluptatem accusantium doloremque laudantium, totam rem aperiam, eaque ipsa quae ab illo inventore veritatis et quasi architecto beatae vitae dicta sunt explicabo. Nemo enim ipsam voluptatem quia voluptas sit aspernatur aut odit aut fugit, sed quia consequuntur magni dolores eos qui ratione voluptatem sequi nesciunt.</p>
  <p>Neque porro quisquam est, qui dolorem ipsum quia dolor sit amet, consectetur, adipisci velit, sed quia non numquam eius modi tempora incidunt ut labore et dolore magnam aliquam quaerat voluptatem. Ut enim ad minima veniam adipisci velit, sed quia non numquam</p>
</div>
<span class="btn" style="left:107px;top:1395px">Learn More</span>
<div class="abs about-photo" role="img" aria-label="Yellow industrial dewatering pump with hoses"></div>

<!-- Products -->
<h2 class="sec-title" style="top:1487px">Our Products</h2>
<div class="arrows" style="top:1503px"><span><svg width="8" height="10" viewBox="0 0 8 10"><path d="M6 1 2 5l4 4" fill="none" stroke="#333" stroke-width="1.6"/></svg></span><span><svg width="8" height="10" viewBox="0 0 8 10"><path d="m2 1 4 4-4 4" fill="none" stroke="#333" stroke-width="1.6"/></svg></span></div>
<div class="product" style="left:85px"><div class="photo" role="img" aria-label="Orange trailer-mounted dewatering pump" style="background:radial-gradient(circle at 50% 50%,#e0601c 0%,#c4501a 40%,#fff 75%)"></div></div>
<div class="product active" style="left:349px"><div class="photo" role="img" aria-label="Teal centrifugal pump" style="background:radial-gradient(circle at 50% 50%,#3fb8c6 0%,#12a8d3 70%)"></div><span class="btn" style="left:67px;top:103px">View Details</span></div>
<div class="product" style="left:614px"><div class="photo" role="img" aria-label="Blue electric surface pump" style="background:radial-gradient(circle at 50% 50%,#2b3f5c 0%,#4b6a8c 35%,#fff 70%)"></div></div>
<div class="product" style="left:876px"><div class="photo" role="img" aria-label="Coil of yellow corrugated drainage pipe" style="background:radial-gradient(ellipse at 50% 50%,#f2d22e 0%,#e2b70e 40%,#fff 72%)"></div></div>
<span class="product-name" style="left:85px">Dewatering Pump</span>
<span class="product-name" style="left:349px">Dewatering Pump</span>
<span class="product-name" style="left:614px">Dewatering Pump</span>
<span class="product-name" style="left:876px">Dewatering Pump</span>

<!-- Projects -->
<div class="abs projects"></div>
<h2 class="sec-title" style="top:1928px">Our Projects</h2>
<div class="arrows" style="top:1944px"><span><svg width="8" height="10" viewBox="0 0 8 10"><path d="M6 1 2 5l4 4" fill="none" stroke="#333" stroke-width="1.6"/></svg></span><span><svg width="8" height="10" viewBox="0 0 8 10"><path d="m2 1 4 4-4 4" fill="none" stroke="#333" stroke-width="1.6"/></svg></span></div>
<div class="project">
  <div class="photo" style="left:85px;background:linear-gradient(160deg,#8b7d66,#5d5546 60%,#3e3a33)" role="img" aria-label="Excavated trench with orange dewatering pipe"></div>
  <h4 style="left:85px">natus error sit voluptatem</h4><p style="left:85px">Sed ut perspiciatis unde omnis iste natus</p>
</div>
<div class="project">
  <div class="photo" style="left:437px;background:linear-gradient(160deg,#9a8f7b,#6f6a5d 55%,#3f5a66)" role="img" aria-label="Crew installing large blue valve in excavation"></div>
  <h4 style="left:437px">natus error sit voluptatem</h4><p style="left:437px">Sed ut perspiciatis unde omnis iste natus</p>
</div>
<div class="project">
  <div class="photo" style="left:788px;background:linear-gradient(160deg,#7a6a55,#3b3a38 55%,#24262a)" role="img" aria-label="Large black pipes laid in a trench"></div>
  <h4 style="left:788px">natus error sit voluptatem</h4><p style="left:788px">Sed ut perspiciatis unde omnis iste natus</p>
</div>

<!-- Testimonials -->
<h2 class="sec-title" style="top:2463px">Clients Say</h2>
<div class="arrows" style="top:2478px"><span><svg width="8" height="10" viewBox="0 0 8 10"><path d="M6 1 2 5l4 4" fill="none" stroke="#333" stroke-width="1.6"/></svg></span><span><svg width="8" height="10" viewBox="0 0 8 10"><path d="m2 1 4 4-4 4" fill="none" stroke="#333" stroke-width="1.6"/></svg></span></div>
<div class="quote" style="left:85px">Sed ut perspiciatis unde omnis iste natus error sit voluptatem accusantium doloremque laudantium, totam rem aperiam, eaque ipsa quae ab illo inventore veritatis et quasi architecto beatae vitae dicta sunt explicabo. Nemo enim ipsam voluptatem quia</div>
<div class="quote" style="left:614px">Sed ut perspiciatis unde omnis iste natus error sit voluptatem accusantium doloremque laudantium, totam rem aperiam, eaque ipsa quae ab illo inventore veritatis et quasi architecto beatae vitae dicta sunt explicabo. Nemo enim ipsam voluptatem quia</div>
<div class="avatar" style="left:100px" role="img" aria-label="Client portrait"></div>
<span class="author" style="left:168px">Della M. Oakes</span>
<div class="avatar" style="left:629px" role="img" aria-label="Client portrait"></div>
<span class="author" style="left:696px">Della M. Oakes</span>

<!-- Clients -->
<h2 class="sec-title" style="top:2768px">Our Clients</h2>
<div class="abs clients">
  <div><i></i>Arvenoth</div>
  <div><i></i>Plimsora</div>
  <div><i></i>Quellbrook</div>
  <div><i></i>Tavrenex</div>
  <div><i></i>Ombrevale</div>
  <div>Kestrano</div>
</div>

<!-- Footer -->
<footer class="abs footer">
  <div class="flogo">Quorvantelline.com</div>
  <div class="tag">Sed ut perspiciatis unde omnis</div>
  <p class="ftext">Sed ut perspiciatis unde omnis iste natus error sit voluptatem accusantium doloremque laudantium, totam rem aperiam, eaque ipsa quae ab illo inventore veritatis et quasi architecto beatae vitae dicta sunt explicabo.</p>
  <div class="social"><span></span><span></span><span></span></div>
  <div class="contact">
    <h5>CONTACT DETAILS</h5>
    <svg class="abs" style="left:878px;top:82px" width="12" height="16" viewBox="0 0 12 16"><path d="M6 0a6 6 0 0 0-6 6c0 4.5 6 10 6 10s6-5.5 6-10a6 6 0 0 0-6-6zm0 8.5A2.5 2.5 0 1 1 6 3.5a2.5 2.5 0 0 1 0 5z" fill="#fff"/></svg>
    <div class="addr"><b>Quorvantelline</b> 2210 Palmetto Row<br>Suite 310, Tampa FL 33602</div>
    <div class="tel" style="left:878px"><svg width="14" height="12" viewBox="0 0 14 12"><rect x="1" y="3" width="12" height="9" rx="1" fill="#fff"/><rect x="3" y="0" width="8" height="4" fill="#fff"/></svg>813.555.0147</div>
    <div class="tel" style="left:1000px"><svg width="14" height="14" viewBox="0 0 24 24"><path d="M6.6 10.8a15 15 0 0 0 6.6 6.6l2.2-2.2a1 1 0 0 1 1-.25 11 11 0 0 0 3.6.6 1 1 0 0 1 1 1V20a1 1 0 0 1-1 1A17 17 0 0 1 3 4a1 1 0 0 1 1-1h3.5a1 1 0 0 1 1 1 11 11 0 0 0 .6 3.6 1 1 0 0 1-.25 1z" fill="#fff"/></svg>813.555.0192</div>
  </div>
</footer>
<div class="abs copy">© Copyright 2018.All rights reserved. <a href="#">Privacy Policy</a></div>

</body>
</html>
```